Flyer Design Project

Need a creative flyer design for a new coffee shop. The name of the coffee shop is Plum Kettle. We sell coffees, teas, espresso based drinks, pastries and freshly made mini donuts.
Looking for the flyer to have the following:
1. Now Open
2. advertisement: try our freshly made mini donuts 6 for $1
3. advertisement: 1/2 price coffee Monday's
4. address: 938 north 6th street, Roselle, NJ 07215
5. pictures of coffee and lattes
6. the logo
7. offers end June 30, 2013
8. Free Wifi
Feel free to be creative. I want the flyer to be eye catching. Open to different sizes and shapes to the flyer.
Note: flyer can be one or two sided. I do not have any additional photos.
Industry/Entity Type
Coffee Shop
Look and feel
Each slider illustrates characteristics of the customer's brand and the style your logo design should communicate.

```html
<!DOCTYPE html>
<html lang="en">
<head>
<meta charset="utf-8">
<title>Plum Kettle – Now Open</title>
<link rel="stylesheet" href="https://fonts.googleapis.com/css2?family=Josefin+Sans:wght@400;700&family=Jost:wght@500;600;700&family=Ubuntu:wght@500&display=swap">
<style>
  :root {
    --orange: #f5892e;
    --ink: #000000;
    --paper: #ffffff;
    --roast: #3f2713;
    --frame: #000000;
  }
  html, body {
    margin: 0;
    padding: 0;
    width: 933px;
    height: 1200px;
    overflow: hidden;
    background: var(--frame);
  }
  .flyer {
    position: relative;
    width: 933px;
    height: 1200px;
    overflow: hidden;
    font-family: "Jost", "Futura", sans-serif;
  }
  .flyer__shapes {
    position: absolute;
    left: 0;
    top: 0;
    width: 933px;
    height: 1200px;
  }
  .headline {
    position: absolute;
    left: 0;
    right: 0;
    top: 87px;
    margin: 0;
    text-align: center;
    white-space: nowrap;
    font-family: "Josefin Sans", "Futura", sans-serif;
    font-weight: 700;
    font-size: 140px;
    line-height: 1;
    letter-spacing: -3px;
    color: var(--paper);
    text-shadow: -8px 7px 0 var(--ink);
  }
  .offer-line {
    position: absolute;
    right: 72px;
    margin: 0;
    white-space: nowrap;
    text-align: right;
    text-transform: uppercase;
    line-height: 1;
  }
  .offer-line--intro { top: 601px; font-weight: 700; font-size: 40px; color: var(--ink); }
  .offer-line--item  { top: 628px; font-weight: 700; font-size: 70px; color: var(--ink); }
  .offer-line--price { top: 695px; font-weight: 600; font-size: 88px; color: var(--orange); }
  .offer-line--half  { top: 802px; font-weight: 700; font-size: 80px; color: var(--ink); }
  .offer-line--day   { top: 897px; font-weight: 600; font-size: 44px; color: var(--orange); }

  .brand {
    position: absolute;
    left: 66px;
    top: 970px;
  }
  .brand__name {
    margin: 0;
    white-space: nowrap;
    font-family: "Josefin Sans", "Futura", sans-serif;
    font-weight: 700;
    font-size: 76px;
    line-height: 1;
    letter-spacing: -1px;
    text-transform: uppercase;
    color: var(--roast);
  }
  .brand__tagline {
    margin: 30px 0 0 86px;
    white-space: nowrap;
    font-family: "Ubuntu", sans-serif;
    font-weight: 500;
    font-size: 34px;
    line-height: 1;
    color: var(--paper);
  }
  .address {
    position: absolute;
    left: 607px;
    top: 975px;
    margin: 0;
    white-space: nowrap;
    font-family: "Josefin Sans", "Futura", sans-serif;
    font-style: normal;
    font-weight: 400;
    font-size: 23px;
    line-height: 32px;
    text-transform: uppercase;
    color: var(--ink);
  }
  .fine-print {
    position: absolute;
    left: 636px;
    top: 1096px;
    margin: 0;
    white-space: nowrap;
    font-family: "Josefin Sans", "Futura", sans-serif;
    font-size: 16px;
    line-height: 1;
    letter-spacing: 0.3px;
    text-transform: uppercase;
    color: var(--paper);
  }
</style>
</head>
<body>
<main class="flyer">
  <svg class="flyer__shapes" viewBox="0 0 900 1157" preserveAspectRatio="none">
    <defs>
      <clipPath id="panel-clip">
        <path d="M270 240 L888 240 L888 1040 L610 1040 C510 1040 465 940 450 870 C420 730 130 700 130 565 L130 380 C130 300 190 240 270 240 Z"/>
      </clipPath>
      <radialGradient id="photo-tone" cx="0.68" cy="0.45" r="0.7">
        <stop offset="0" stop-color="#5b5b5b"/>
        <stop offset="0.55" stop-color="#2a2a2a"/>
        <stop offset="1" stop-color="#121212"/>
      </radialGradient>
    </defs>
    <rect class="frame" x="0" y="0" width="900" height="1157" fill="#000000"/>
    <rect class="sheet" x="12" y="12" width="876" height="1133" fill="#f5892e"/>
    <path class="panel" fill="#ffffff" d="M270 240 L888 240 L888 1040 L610 1040 C510 1040 465 940 450 870 C420 730 130 700 130 565 L130 380 C130 300 190 240 270 240 Z"/>
    <g clip-path="url(#panel-clip)" role="img" aria-label="Steaming white cup of coffee on a saucer among roasted coffee beans and cinnamon sticks">
      <rect x="0" y="230" width="900" height="335" fill="url(#photo-tone)"/>
    </g>
  </svg>

  <h1 class="headline">NOW OPEN!</h1>

  <section class="offers">
    <p class="offer-line offer-line--intro">Try our freshly made</p>
    <p class="offer-line offer-line--item">Mini donuts</p>
    <p class="offer-line offer-line--price">6 for $1</p>
    <p class="offer-line offer-line--half">1/2 price</p>
    <p class="offer-line offer-line--day">Coffee Mondays</p>
  </section>

  <div class="brand">
    <p class="brand__name">Plum Kettle</p>
    <p class="brand__tagline">Home of the mini donut</p>
  </div>

  <address class="address">938 North 6th Street<br>Roselle, NJ&nbsp;&nbsp;07215</address>

  <p class="fine-print">Offers end June 30, 2013</p>
</main>
</body>
</html>
```